HomePage Design for Lumen Getaways - once-in-a-lifetime experiences for busy working people

Design a homepage for the Lumen Getaways (www.lumengetaways.example) website compatible with further web pages and the design briefing documents attached

LG HomePage Design Brief
We are seeking website HomePage designs incorporating our new Logo and colour scheme, for Lumen Getaways (www.lumengetaways.example) to go with the site functionality and wireframe ideas attached.
The website HomePage design needs to
• Incorporate and be consistent with the LG Logo and its colour scheme attached.
• Express the brand values of being inspirational, high quality, upscale, cultured, aspirational, and contemporary – even somewhat ‘hip’. Probably positioned somewhere between Harlow Pike (Deluxe Travel) and Green Walrus (Hip Travel) – see https://www.harlowpike.example and https://www.greenwalrus.example .
• Be instantly recognisable and different from other travel websites and instantly communicate the nature of the brand proposition and target customer base.
• Appeal to our core 25-55 affluent businesspeople demographic
• Work in the UK, US/Canada and Australia/NZ and ultimately in mainland Europe.
• Use fonts and colours that are easily reproduced online and compatible with nearly all browsers.
• Be part of a responsive website design, that can be used both on Desktops and laptops but also with tablets and mobile ‘phones (hence content not too wide across the page)
• Feature the strapline ‘Lumen Getaways in less than 7 Days’
• Work with the and wireframes and processes shown in the attached presentation – although intended as a guide only these features and processes all need to be incorporated into the HomePage.
• Make full use of high quality images and video to convey our brand proposition and products

Target Market(s)

25-55 affluent businesspeople

Industry/Entity Type

Travel Industry

Number of Pages Required

1 page

Font styles to use
Sans Serif

Colors
0455a3
00a88f

Requirements
Must have
• • Incorporate and be consistent with the LG Logo and its colour scheme attached.
• • Express the brand values of being inspirational, high quality, upscale, cultured, aspirational, and contemporary – even somewhat ‘hip’. Probably positioned somewhere between Harlow Pike (Deluxe Travel) and Green Walrus (Hip Travel) – see https://www.harlowpike.example and https://www.greenwalrus.example .
• • Be instantly recognisable and different from other travel websites and instantly communicate the nature of the brand proposition and target customer base.
• • Appeal to our core 25-55 affluent businesspeople demographic
• • Be part of a responsive website design, that can be used both on Desktops and laptops but also with tablets and mobile ‘phones (hence content not too wide across the page)
• • Feature the strapline ‘Lumen Getaways in less than 7 Days’
• • Work with the and wireframes and processes shown in the attached presentation – although intended as a guide only these features and processes all need to be incorporated into the HomePage.
• • Make full use of high quality images and video to convey our brand proposition and products
• Colours as per Logo not as shown below
Nice to have
• • Work in the UK, US/Canada and Australia/NZ and ultimately in mainland Europe.
Should not have
• Must not be cheap or mass-market, nor excessively "stuffy or luxury-orientated"

```html
<!DOCTYPE html>
<html lang="en">
<head>
<meta charset="utf-8">
<title>Lumen Getaways — Home</title>
<link rel="stylesheet" href="https://fonts.googleapis.com/css2?family=Montserrat:wght@700;800&family=Raleway:wght@500;600;700;800&display=swap">
<style>
  :root {
    --indigo: #35357a;
    --indigo-deep: #2b2b6b;
    --indigo-active: #43439a;
    --green: #167a3c;
    --green-logo: #1f7a3a;
    --red: #c0121c;
    --ink: #2e2e6e;
    --white: #ffffff;
    --caption: #0d5f99;
    --frame: #d6d6e2;
  }
  * { box-sizing: border-box; margin: 0; padding: 0; }
  html, body { width: 1200px; height: 1174px; overflow: hidden; }
  body { font-family: "Raleway", sans-serif; background: var(--white); position: relative; }

  .top-bar {
    position: absolute; left: 0; top: 0; width: 1200px; height: 120px;
    background: linear-gradient(90deg, #e7e3ea 0%, #ece0e0 50%, #f1d6b8 80%, #f3c08c 100%);
  }
  .brand {
    position: absolute; left: 0; width: 1200px; top: 46px; text-align: center;
    display: flex; justify-content: center; align-items: center; gap: 10px;
  }
  .brand-dot { width: 22px; height: 22px; border-radius: 50%; background: var(--indigo); }
  .brand-name { font-weight: 800; font-size: 20px; letter-spacing: 1px; color: var(--green-logo); }
  .follow { position: absolute; left: 871px; top: 95px; display: flex; align-items: center; gap: 10px; }
  .follow-label { font-size: 14px; font-weight: 600; color: #333; margin-right: 4px; }
  .social { width: 22px; height: 22px; border-radius: 50%; background: var(--white); border: 1px solid #d8d8e0; }

  .hero {
    position: absolute; left: 0; top: 120px; width: 1200px; height: 392px;
    background:
      radial-gradient(ellipse at 95% 5%, #f6c987 0%, rgba(246,201,135,0) 45%),
      linear-gradient(180deg, #b490b4 0%, #9c7aa6 35%, #7d6a8c 65%, #5a5a56 100%);
  }
  .hero-title {
    position: absolute; left: 90px; top: 135px;
    font-family: "Montserrat", sans-serif; font-weight: 800; font-size: 41px; line-height: 50px;
    color: var(--white); letter-spacing: 0.5px; text-shadow: 0 2px 6px rgba(0,0,0,0.25);
  }
  .search { position: absolute; left: 87px; top: 265px; width: 371px; height: 43px; display: flex;
    border: 2px solid #e8e8ee; }
  .search-input { flex: 1; background: var(--white); font-size: 13px; color: #999; padding: 0 0 0 24px; line-height: 39px; }
  .search-btn { width: 70px; background: var(--green); color: var(--white); font-weight: 700; font-size: 13px; text-align: center; line-height: 39px; }

  .slider { position: absolute; left: 714px; top: 73px; width: 347px; height: 222px; box-shadow: 0 4px 12px rgba(0,0,0,0.3); }
  .slide-photo { width: 100%; height: 191px;
    background: linear-gradient(110deg, #b3161a 0%, #d23a26 40%, #5d90c8 60%, #f1b05a 100%); }
  .slide-caption { height: 31px; background: var(--caption); color: var(--white); font-weight: 700; font-size: 13px;
    text-align: center; line-height: 31px; }
  .slide-caption b { font-size: 16px; margin-left: 6px; }
  .slide-caption small { font-size: 12px; }
  .slider-arrow { position: absolute; top: 172px; }
  .slider-dots { position: absolute; left: 864px; top: 299px; display: flex; gap: 6px; }
  .slider-dots span { width: 7px; height: 7px; border-radius: 50%; background: var(--white); }
  .slider-dots span.on { background: var(--caption); }

  .main-nav { position: absolute; left: 0; top: 512px; width: 1200px; height: 68px; background: var(--indigo);
    display: flex; padding-left: 86px; }
  .nav-item { color: var(--white); font-weight: 700; font-size: 14px; letter-spacing: 0.3px; line-height: 68px;
    text-align: center; border-right: 1px solid rgba(255,255,255,0.15); }
  .nav-item:last-child { border-right: none; }
  .nav-item.active { background: var(--indigo-active); }

  .region-menu { position: absolute; left: 86px; top: 581px; width: 254px; z-index: 3;
    background: var(--white); box-shadow: 0 3px 8px rgba(0,0,0,0.25); }
  .region { height: 41px; line-height: 41px; padding-left: 20px; font-size: 14px; font-weight: 500; color: var(--ink);
    border-bottom: 1px solid #ccc; }
  .region.active { background: var(--indigo-deep); color: var(--white); position: relative; }
  .region.active::after { content: ""; position: absolute; right: -11px; top: 13px;
    border-left: 11px solid var(--indigo-deep); border-top: 8px solid transparent; border-bottom: 8px solid transparent; }
  .country-menu { position: absolute; left: 340px; top: 581px; width: 123px; height: 212px; z-index: 2;
    background: var(--white); box-shadow: 2px 3px 8px rgba(0,0,0,0.25); padding-top 8px;
    text-align: center; padding-top: 9px; }
  .country { font-size: 12px; font-weight: 700; color: var(--ink); line-height: 17px; letter-spacing: 0.4px; }
  .country.current { color: var(--green); }

  .tile { position: absolute; width: 173px; height: 149px; box-shadow: 0 2px 5px rgba(0,0,0,0.3); background: var(--white); }
  .tile-head { height: 28px; background: var(--green); color: var(--white); font-size: 12.5px; font-weight: 600;
    text-align: center; border-radius: 3px 3px 0 0; display: flex; align-items: center; justify-content: center; line-height: 13px; }
  .tile-photo { height: 117px; margin: 2px; }

  .promo { position: absolute; left: 898px; width: 214px; height: 150px; }
  .promo-head { height: 27px; background: var(--red); color: var(--white); font-size: 12.5px; font-weight: 700;
    padding: 0 8px 0 14px; display: flex; justify-content: space-between; align-items: center; }
  .promo-head span:last-child { font-size: 11px; font-weight: 600; }
  .promo-photo { height: 123px; }

  .site-footer { position: absolute; left: 0; top: 1082px; width: 1200px; height: 92px;
    background: linear-gradient(90deg, #5f5a98 0%, #6b5a9c 50%, #7a5c9c 100%); color: var(--white); }
  .foot-col { position: absolute; top: 16px; }
  .foot-col h3 { font-size: 15px; font-weight: 700; margin-bottom: 5px; }
  .foot-col p { font-size: 12.5px; font-weight: 600; line-height: 16px; padding-left: 12px; }
  .foot-col.wide h3 { line-height: 16px; }
  .foot-col.wide p { padding-left: 2px; font-size: 14px; margin-top: 18px; }
</style>
</head>
<body>

<header class="top-bar">
  <div class="brand"><span class="brand-dot"></span><span class="brand-name">LUMEN GETAWAYS</span></div>
  <div class="follow">
    <span class="follow-label">Follow Us:</span>
    <span class="social" aria-label="Social link"></span>
    <span class="social" aria-label="Social link"></span>
    <span class="social" aria-label="Social link"></span>
    <span class="social" aria-label="Social link"></span>
    <span class="social" aria-label="Social link"></span>
  </div>
</header>

<section class="hero" role="img" aria-label="Hiker with raised arms on a rocky summit above misty mountains at sunset">
  <h1 class="hero-title">LUMEN GETAWAYS<br>IN LESS THAN 7 DAYS!</h1>
  <div class="search">
    <div class="search-input">Search a Trip</div>
    <div class="search-btn">SEARCH</div>
  </div>
  <svg class="slider-arrow" style="left:692px" width="14" height="24" viewBox="0 0 14 24"><path d="M11 3 L3 12 L11 21" fill="none" stroke="#1366a8" stroke-width="3"/></svg>
  <div class="slider">
    <div class="slide-photo" role="img" aria-label="Masked carnival figure in red feathers beside gondolas on a Venetian lagoon"></div>
    <div class="slide-caption">Venice Festival <b>£ 599</b> <small>pp</small></div>
  </div>
  <svg class="slider-arrow" style="left:1071px" width="14" height="24" viewBox="0 0 14 24"><path d="M3 3 L11 12 L3 21" fill="none" stroke="#1366a8" stroke-width="3"/></svg>
  <div class="slider-dots"><span class="on"></span><span></span><span></span><span></span></div>
</section>

<nav class="main-nav">
  <div class="nav-item active" style="width:124px">DESTINATION</div>
  <div class="nav-item" style="width:130px">EXPERIENCES</div>
  <div class="nav-item" style="width:148px">TRIPS BY MONTH</div>
  <div class="nav-item" style="width:130px">TOPICAL NOW</div>
  <div class="nav-item" style="width:102px">TAILORED</div>
  <div class="nav-item" style="width:146px">PIONEERS CLUB</div>
  <div class="nav-item" style="width:74px">LOGIN</div>
  <div class="nav-item" style="width:178px">VLOGS AND REVIEWS</div>
</nav>

<div class="region-menu">
  <div class="region active">Europe and Middle East</div>
  <div class="region">Asia &amp; Indian sub-Continent</div>
  <div class="region">Latin &amp; Central America</div>
  <div class="region">North America &amp; Canada</div>
  <div class="region">Africa</div>
  <div class="region">Australasia &amp; Pacific</div>
</div>
<div class="country-menu">
  <div class="country">UK</div>
  <div class="country">ITALY</div>
  <div class="country">SPAIN</div>
  <div class="country">GREECE</div>
  <div class="country current">ICELAND</div>
  <div class="country">NORWAY</div>
  <div class="country">SWEDEN</div>
  <div class="country">GREENLAND</div>
  <div class="country">EGYPT</div>
  <div class="country">JORDAN</div>
  <div class="country">ISRAEL</div>
</div>

<div class="tile" style="left:315px;top:657px">
  <div class="tile-head">Festival</div>
  <div class="tile-photo" role="img" aria-label="Glowing lanterns released into the night sky" style="background:linear-gradient(160deg,#3a2412,#b8692a 60%,#2a1a10)"></div>
</div>
<div class="tile" style="left:497px;top:657px">
  <div class="tile-head">Must Do Activities</div>
  <div class="tile-photo" role="img" aria-label="Group sledging down a snowy slope" style="background:linear-gradient(180deg,#5d8fc8,#a9c4e0 50%,#f0f3f7)"></div>
</div>
<div class="tile" style="left:679px;top:657px">
  <div class="tile-head">Unique Annual Event</div>
  <div class="tile-photo" role="img" aria-label="Hot air balloons lit up at a dusk balloon fiesta" style="background:linear-gradient(180deg,#6f8ec0,#d57a3a 55%,#3a2a22)"></div>
</div>
<div class="tile" style="left:229px;top:852px">
  <div class="tile-head">Extraordinary &amp; Secret Places</div>
  <div class="tile-photo" role="img" aria-label="Ruined stone castle beside a moat" style="background:linear-gradient(180deg,#dfe5ee,#8d8576 55%,#5d7a3a)"></div>
</div>
<div class="tile" style="left:411px;top:852px">
  <div class="tile-head">Unforgettable Performances</div>
  <div class="tile-photo" role="img" aria-label="Costumed cast performing on a theatre stage" style="background:linear-gradient(180deg,#3a2030,#b06a5a 50%,#d8a8b0)"></div>
</div>
<div class="tile" style="left:592px;top:852px">
  <div class="tile-head">Spectacular Hiking,<br>Climbing &amp; Walking</div>
  <div class="tile-photo" role="img" aria-label="Climber on an overhanging rock face against blue sky" style="background:linear-gradient(180deg,#2d5fb8,#5a8ad6 60%,#7f8fa0)"></div>
</div>

<aside>
  <div class="promo" style="top:600px">
    <div class="promo-head"><span>Special Offer</span><span>view</span></div>
    <div class="promo-photo" role="img" aria-label="Fireworks bursting over a night sky" style="background:radial-gradient(circle at 40% 40%,#8a2a5a,#2a1230 45%,#0c0a12)"></div>
  </div>
  <div class="promo" style="top:756px">
    <div class="promo-head"><span>Save 20% on this Trip</span><span>view</span></div>
    <div class="promo-photo" role="img" aria-label="Whitewashed hillside village with blue domes above the sea at sunset" style="background:linear-gradient(180deg,#f0c270,#8aa0c0 40%,#e8eef4 75%,#2f5f9a)"></div>
  </div>
  <div class="promo" style="top:911px">
    <div class="promo-head"><span>Featured Place</span><span>view</span></div>
    <div class="promo-photo" role="img" aria-label="Castle ruins on a green clifftop above a deep blue sea" style="background:linear-gradient(180deg,#2a7ad0,#1e88c8 40%,#5b8a3a 70%,#2a6fa8)"></div>
  </div>
</aside>

<footer class="site-footer">
  <div class="foot-col" style="left:87px"><h3>About Us</h3><p>Our Partners</p><p>Newsletter</p><p>FAQs</p></div>
  <div class="foot-col" style="left:213px"><h3>Contact Us</h3><p>Booking Conditions</p><p>Privacy and Cookies</p><p>Terms of Use</p></div>
  <div class="foot-col" style="left:389px"><h3>Financial Protection</h3><p>Travel Insurance</p><p>Visas</p><p>Travel Advice</p></div>
  <div class="foot-col" style="left:592px"><h3>Group Bookings</h3><p>Tailor-made &amp; Extra Nights</p><p>Booking Flights</p><p>Careers with LG</p></div>
  <div class="foot-col wide" style="left:830px"><h3>LG Protecting wildlife &amp; animals,<br>and supporting local communities</h3><p>Press Room</p></div>
</footer>

</body>
</html>
```